Bauzaun-Banner für Abbruchfirma und Schadstoffsanierung
Zielgruppe
Abbruchfirma und Schadstoffsanierung
Aufgabenstellung
Unsere Logo und die Tätigkeiten die wir anbieten müssen vertreten sein
Wir möchten einen Banner für einen Bauzaun entwickeln lassen. Maße sind 340cm x 173 cm

```html
<!DOCTYPE html>
<html lang="de">
<head>
<meta charset="utf-8">
<title>Bauzaun-Banner – Haus und BauService</title>
<link href="https://fonts.googleapis.com/css2?family=Archivo+Black&family=Roboto+Condensed:wght@400;700;800&display=swap" rel="stylesheet">
<style>
  :root{
    --ink:#111;
    --paper:#fff;
    --grey-light:#e6e6e6;
    --grey-mid:#9a9a9a;
    --grey-dark:#3a3a3a;
    --band:#141414;
    --accent:#d8321f;
  }
  *{box-sizing:border-box;margin:0;padding:0}
  html,body{width:1200px;height:683px;overflow:hidden;background:var(--paper)}
  .banner{position:relative;width:1200px;height:683px;background:var(--paper);color:var(--ink);font-family:"Roboto Condensed",sans-serif;overflow:hidden}
  .title{position:absolute;top:22px;left:0;width:100%;text-align:center;font-family:"Archivo Black",sans-serif;font-size:68px;letter-spacing:-1px}
  .service{position:absolute;top:118px;width:520px}
  .service--left{left:40px}
  .service--right{left:640px}
  .service__head{display:flex;align-items:center;gap:14px;font-family:"Archivo Black",sans-serif;font-size:38px;line-height:1.05;text-transform:uppercase}
  .service__icon{flex:none;width:34px;height:34px}
  .service__text{margin:10px 0 0 48px;font-size:16px;line-height:1.45;color:var(--grey-dark)}
  .icon-row{position:absolute;top:268px;left:640px;display:flex;gap:22px}
  .icon-row svg{width:40px;height:40px}
  .brand{position:absolute;top:330px;left:640px;display:flex;align-items:center;gap:14px;font-family:"Roboto Condensed",sans-serif;font-weight:800;font-size:34px}
  .brand__dot{width:40px;height:40px;border-radius:50%;background:var(--ink)}
  .scene{position:absolute;left:0;top:390px;width:1200px;height:175px;background:linear-gradient(180deg,var(--grey-light) 0%,var(--grey-mid) 100%)}
  .scene__building{position:absolute;left:0;top:-60px;width:520px;height:235px;background:linear-gradient(160deg,#2a2a2a,#0e0e0e)}
  .building-name{position:absolute;left:40px;top:28px;color:var(--paper);font-family:"Archivo Black",sans-serif;font-size:64px;line-height:1}
  .building-name small{display:block;font-family:"Roboto Condensed",sans-serif;font-weight:700;font-size:20px;letter-spacing:2px;margin-top:4px}
  .footer{position:absolute;left:0;bottom:0;width:1200px;height:118px;background:var(--band);color:var(--paper);display:flex;align-items:center;padding:0 40px}
  .footer__small{font-family:"Archivo Black",sans-serif;font-size:30px;width:330px}
  .footer__main{flex:1}
  .footer__name{font-family:"Archivo Black",sans-serif;font-size:54px;line-height:1}
  .footer__sub{font-size:26px;font-weight:700;letter-spacing:3px;text-transform:uppercase}
</style>
</head>
<body>
<main class="banner">
  <h1 class="title">Haus und BauService</h1>

  <section class="service service--left">
    <h2 class="service__head">
      <svg class="service__icon" viewBox="0 0 34 34"><circle cx="17" cy="17" r="16" fill="var(--ink)"/><path d="M10 17l5 5 9-10" stroke="#fff" stroke-width="3" fill="none"/></svg>
      Schadstoff<br>Sanierung
    </h2>
    <p class="service__text">Asbest, PCB und KMF fachgerecht entfernt<br>Messung, Planung und sichere Entsorgung</p>
  </section>

  <section class="service service--right">
    <h2 class="service__head">
      <svg class="service__icon" viewBox="0 0 34 34"><circle cx="17" cy="17" r="16" fill="var(--ink)"/><path d="M10 17l5 5 9-10" stroke="#fff" stroke-width="3" fill="none"/></svg>
      Abbruch<br>Entsorgung
    </h2>
    <p class="service__text">Rückbau von Gebäuden aller Größen<br>Container und Abfuhr aus einer Hand</p>
  </section>

  <div class="icon-row" aria-hidden="true">
    <svg viewBox="0 0 40 40"><circle cx="20" cy="20" r="19" fill="var(--ink)"/><path d="M12 21l6 6 11-13" stroke="#fff" stroke-width="3" fill="none"/></svg>
    <svg viewBox="0 0 40 40"><circle cx="20" cy="20" r="19" fill="var(--ink)"/><path d="M11 20h16m-6-6l6 6-6 6" stroke="#fff" stroke-width="3" fill="none"/></svg>
    <svg viewBox="0 0 40 40"><circle cx="20" cy="20" r="19" fill="var(--ink)"/><path d="M20 10c-5 0-8 4-8 8 0 6 8 13 8 13s8-7 8-13c0-4-3-8-8-8z" fill="#fff"/><circle cx="20" cy="18" r="3" fill="var(--ink)"/></svg>
    <svg viewBox="0 0 40 40"><circle cx="20" cy="20" r="19" fill="var(--ink)"/><path d="M12 21l6 6 11-13" stroke="#fff" stroke-width="3" fill="none"/></svg>
  </div>

  <div class="brand"><span class="brand__dot"></span>NR-Velden</div>

  <div class="scene" role="img" aria-label="Illustration: Firmengebäude, Absperrkegel und Kipper-Lkw vor einer Stadtkulisse">
    <div class="scene__building">
      <p class="building-name">NRV<small>BAU-SERVICE</small></p>
    </div>
  </div>

  <footer class="footer">
    <p class="footer__small">NR-VELDEN</p>
    <div class="footer__main">
      <p class="footer__name">NR-VELDEN</p>
      <p class="footer__sub">Haus und BauService 340 × 173 cm</p>
    </div>
  </footer>
</main>
</body>
</html>
```